Vascular Secialist needs a tri-fold brochure

I would like to create a tri- fold of all the services that the vascular practice offers. The practice specializes in lower extremity vascular diseases. I would like to have the tri-fold have brief descriptions of all the services as well as images of the practice to show case the top of the line technology. The trip-fold will be front in back with a crisp modern design. The diseases that they treat are: arterial disease, venous disease, varicose veins, chronic venous insufficiency, deep vein thrombosis, uterine fibroids, pelvic and labial varicose veins, varicocele. Treatment options for all diseases that the practice treats.

Target Market(s)

Doctors

Industry/Entity Type

Medical

Other font styles liked:
• Myriod Pro SemiExtende

Colors
33a6d7
86cae7
aaaaaa
85cae6
dcedf6
cee9f5
757575
9d9d9d
c3c3c3

Requirements
Must have
• creativity and taglines that capture the reader
Nice to have
• I would like the piece to mirror the website. www.lumavexclinic.example

```html
<!DOCTYPE html>
<html lang="en">
<head>
<meta charset="utf-8">
<title>Lumavex – Diseases Treated</title>
<link href="https://fonts.googleapis.com/css2?family=Source+Sans+3:ital,wght@0,400;0,600;0,700;1,400;1,600&display=swap" rel="stylesheet">
<style>
  :root{
    --brand-blue:#1f77b9;
    --header-blue:#1c75bc;
    --soft-blue:#5ba3d6;
    --story-blue:#2a8ccd;
    --panel-bg:#dcedf6;
    --text:#231f20;
    --white:#ffffff;
    --vein-light:#86cae7;
    --vein-dark:#2c4a7a;
  }
  *{margin:0;padding:0;box-sizing:border-box}
  html,body{width:1200px;height:929px;overflow:hidden;background:var(--white)}
  body{font-family:"Source Sans 3",sans-serif;color:var(--text);position:relative}
  .brochure{position:relative;width:1200px;height:929px}
  .title-band{position:absolute;left:0;top:0;width:857px;height:66px;background:var(--header-blue)}
  .title-band h1{position:absolute;left:37px;top:20px;color:var(--white);font-size:22px;font-weight:700;font-style:italic;letter-spacing:-0.2px}
  .column{position:absolute;top:88px;width:236px;font-size:13.3px;line-height:18.2px;text-align:justify}
  .col-one{left:50px}
  .col-two{left:331px}
  .col-three{left:611px}
  .column p{margin-bottom:18px}
  .disease-title{position:relative;display:block;font-size:17px;font-weight:700;line-height:19px;color:var(--brand-blue);text-align:left}
  .disease-title.inline{display:inline;}
  .disease-title.light{color:var(--soft-blue)}
  .disease-title::before{content:"";position:absolute;left:-11px;top:5px;border-left:5px solid currentColor;border-top:5px solid transparent;border-bottom:5px solid transparent}
  .story-panel{position:absolute;left:866px;top:0;width:334px;height:929px;background:var(--panel-bg)}
  .story-photo{position:absolute;left:1044px;top:0;width:156px;height:190px;background:linear-gradient(160deg,#b9b2ac,#7d7671 60%,#4e4a47)}
  .story-title{position:absolute;left:882px;top:34px;font-size:23px;font-weight:600;color:var(--text)}
  .story-lead{position:absolute;left:882px;top:66px;width:150px;font-size:14.2px;line-height:20.8px;font-style:italic;color:var(--story-blue);text-align:justify}
  .story-body{position:absolute;left:882px;top:204px;width:310px;font-size:13.3px;line-height:19.2px;text-align:justify}
  .story-body p{margin-bottom:14px}
  .vessel{position:absolute;top:654px;height:218px;border-radius:4px}
  .vessel.before{left:923px;width:90px;background:linear-gradient(90deg,var(--vein-light),var(--vein-dark) 25%,#3d5c8f 50%,var(--vein-dark) 75%,var(--vein-light))}
  .vessel.after{left:1040px;width:106px;background:linear-gradient(90deg,var(--vein-light),var(--vein-dark) 25%,#3d5c8f 50%,var(--vein-dark) 75%,var(--vein-light))}
  .caption{position:absolute;top:884px;font-size:11.5px;line-height:16px;text-align:center}
  .caption.before{left:903px;width:130px}
  .caption.after{left:1028px;width:130px}
</style>
</head>
<body>
<div class="brochure">
  <header class="title-band"><h1>Diseases treated at Lumavex</h1></header>

  <section class="column col-one">
    <p><span class="disease-title">Peripheral Arterial Disease</span>Peripheral Arterial Disease (PAD) develops when the arteries in the legs build up plaque, obstructing and narrowing the arteries and preventing blood, oxygen, glucose from flowing properly to tissue. This lack of blood-flow causes pain, cramping, and swelling in the legs as the muscles and tissue starve for blood and if untreated, can lead to amputation of the toes and/ or foot.</p>
    <p><span class="disease-title inline light">Varicose Veins</span>&nbsp;&nbsp; Closely related to chronic venous insufficiency, varicose veins are enlarged veins that are visible through the skin. The veins often appear bulging or twisted and are generally larger than three millimeters in diameter. Varicose veins affect one out of two people over the age of 50, and women who have had children are particularly susceptible.</p>
    <p><span class="disease-title">Deep Venous Thrombosis</span>A DVT is the formation of a blood clot (thrombus) in a deep veins, most commonly occurring in the legs. This thrombus disrupts the normal flow of blood from the legs or arms back to the heart. A DVT presents a serious risk to your life; the clot could move to your heart or lungs causing serious and sometimes fatal conditions. You must see a doctor immediately if you think you may have a DVT.</p>
    <p><span class="disease-title light">Varicocele - A male condition</span>A varicocele (VAR-ih-koe-seel) is an enlargement of the veins within the scrotum. A varicocele is similar to a varicose vein that can occur in the legs or in the female pelvic area. 15% of the general male population suffer from varicocele with more than 80%</p>
  </section>

  <section class="column col-two">
    <p>occurring on the left side and the remainder on both sides. They are generally acquired during puberty.</p>
    <p>Most varicoceles are asymptomatic; however, some can cause scrotal pain. This pain is generally mild to moderate, occurs with long periods of sitting, standing or activity and is relieved by lying down. Although it can be uncomfortable before bedtime (after a long day of activity), it generally does not occur upon awakening after a night’s rest. The pain is dull, congestive, “tooth ache” like and generally doesn’t refer elsewhere. The resulting backup causes the veins to widen (dilate) which can lead to damage to the testicle and result in worsened fertility. Our physicians can provide targeted treatment for varicocele called “varicocele repair.”</p>
    <p><span class="disease-title">Pelvic Venous Congestion</span><span class="disease-title inline" style="padding:0">(PVCS)</span>&nbsp;&nbsp; Pelvic venous congestion syndrome (PVCS) also known as ovarian vein reflux, causes chronic pelvic pain in approximately 13-40% of women. The ovarian veins carry venous blood from the ovaries and pelvis up to the level of the renal veins in the abdomen. All veins have valves to help guide blood flow back up towards the heart. When these valves become damaged or dysfunctional, some blood flows backwards causing the veins to become engorged or “congested,’ leading to varicose veins. PVCS is essentially varicose veins in the pelvis due to venous insufficiency in the ovarian veins. These internal varicose veins can cause chronic, debilitating pain. This pressure may also cause visible varicose veins around the vulva, vagina, inner thigh, sometimes the buttocks, and down the leg(s).</p>
  </section>

  <section class="column col-three">
    <p><span class="disease-title light">Pelvic and Labial Varicose Veins</span>Pelvic varicose veins and labial varicose veins are forms of venous insufficiency by which women’s pelvic, labial, or vulvar veins become enlarged and dilated during pregnancy and continue after the baby has been delivered. Such varicosities often worsen with each pregnancy. Some women develop frequent or continuous pain from labial varicosities prominent during pregnancy and improve after the baby is born. Labial varicose veins may be due to iliac vein obstruction from compression or old clots, or they may be due to ovarian vein reflux with pelvic venous insufficiency. In some patients, the primary problem is reflux (abnormal reversal of flow) in the veins of the deep pelvis through veins near the vagina into the labia and surrounding tissues. Like with all types of venous reflux disease, our physicians provided targeted treatments that divert blood flow through healthy veins and eliminate discomfort.</p>
    <p><span class="disease-title inline">Uterine Fibroids</span>&nbsp; Uterine fibroids (fibroid tumors, leiomyomas, or myomas) are benign masses that grow on the outside or in the muscle wall of the uterus. Fibroids are very common in women in their 30s and 40s— as many 70%-80% of all women will have fibroids by age 50. While the cause of Fibroids is not conclusively proven, they seem to be linked with the female hormones estrogen and progesterone. Fibroids can range in number and size from a single growth to multiple growths, and from very small to very large.</p>
  </section>

  <aside class="story-panel" aria-label="Patient story"></aside>
  <div class="story-photo" role="img" aria-label="Portrait photograph of an elderly female patient"></div>
  <h2 class="story-title">Patient Story</h2>
  <p class="story-lead">Female, age 91 referred by her podiatrist for gangrene, non-healing wounds on her toes, and absent pulse in the foot.</p>
  <div class="story-body">
    <p>This patient was referred by her podiatrist for an emergency evaluation of her left foot. The foot was progressively darkening (turning black due to lack of blood flow), had no detectable pulse, and had two non-healing wounds on the toes. Due to her absent arterial flow through the leg, the foot was no longer receiving any oxygen and was quickly dying; she was at a critical risk for amputation. Following her ultrasound, she was immediately scheduled for intervention. Dr. Hallworth treated her arteries with thorough athrectomy, stenting, and angioplasty all the way down into her foot to create a clear arterial blood flow through the limb. With restored blood flow, the color in her foot slowly returned to normal, her pulse returned, and her wounds began to heal.</p>
    <p>Before treatment (image 1) she had no arteries flowing down into the foot causing the slow death of the foot. After extensive treatment (image 2), she had two strong arteries flowing into the foot and she began to recover.</p>
  </div>
  <div class="vessel before" role="img" aria-label="Illustration of a vessel with faulty valve and backward blood flow"></div>
  <div class="vessel after" role="img" aria-label="Illustration of a vessel with restored one-way blood flow"></div>
  <p class="caption before">Image 1<br>Before Treatment</p>
  <p class="caption after">Image 2<br>After Treatment</p>
</div>
</body>
</html>
```